Author needs a new book, Kindle and Audiobook cover design

I updated and re-edited a book I wrote 25 years ago but now realize the title and design did not get the job done. I am seeking a book, Kindle and audiobook design that will make me stand out. The final design will pop while being sensitive to the nature of the subject. The title of the book is Hollow Altars. Subtitle: Leaving Cold Pews Behind and Mending a Wounded Heart Along the Road by Delia R. Marwick. I am wanting to get the attention of people who have been damaged by a church relationship that started well but ended badly.
Updates

The book title is: Hollow Altars. The Subtitle is: Leaving Cold Pews Behind and Mending a Wounded Heart Along The Road. The dimension is 6x9 (150 pages) and I am the author: Delia R. Marwick

Target Market(s)

People with a church experience; church leadership. Religious abuse victims.

Industry/Entity Type

Christian

Font styles to use
Serif

Colors

Designer to choose colors to be used in the design.

Requirements
Nice to have
• I am not married to the Serif font if another design works better.

```html
<!DOCTYPE html>
<html lang="en">
<head>
<meta charset="utf-8">
<title>Hollow Altars — Delia R. Marwick</title>
<link rel="stylesheet" href="https://fonts.googleapis.com/css2?family=Roboto:wght@300;700&family=Roboto+Condensed:wght@700&display=swap">
<style>
  :root {
    --page-bg: #ffffff;
    --cover-dark: #231e1c;
    --cover-mid: #3a3433;
    --haze: #bdbdbd;
    --glow: #f4f4f4;
    --title-red: #ee2a2f;
    --title-white: #ffffff;
    --subtitle: #e4e4e4;
  }
  html, body {
    margin: 0;
    width: 1200px;
    height: 1106px;
    overflow: hidden;
    background: var(--page-bg);
  }
  .canvas {
    position: relative;
    width: 1200px;
    height: 1106px;
  }
  .cover {
    position: absolute;
    left: 267px;
    top: 53px;
    width: 667px;
    height: 1000px;
    background: var(--cover-dark);
    overflow: hidden;
    box-shadow: 0 18px 40px rgba(0,0,0,0.18);
  }
  .cover-art {
    position: absolute;
    inset: 0;
    background:
      radial-gradient(ellipse 34% 30% at 48% 18%, var(--glow) 0%, rgba(220,220,220,0.75) 35%, rgba(150,150,150,0) 100%),
      radial-gradient(ellipse 70% 50% at 50% 25%, rgba(140,136,134,0.85) 0%, rgba(60,54,52,0.6) 55%, rgba(35,30,28,0) 100%),
      linear-gradient(180deg, var(--cover-mid) 0%, var(--cover-dark) 62%, var(--cover-dark) 100%);
  }
  .title-block {
    position: absolute;
    left: 0;
    right: 0;
    top: 615px;
    text-align: center;
    font-family: "Roboto", sans-serif;
    font-weight: 700;
    text-transform: uppercase;
    line-height: 0.9;
  }
  .title-line-1 {
    display: block;
    color: var(--title-red);
    font-size: 104px;
    letter-spacing: -1px;
  }
  .title-line-2 {
    display: block;
    color: var(--title-white);
    font-size: 146px;
    letter-spacing: -2px;
  }
  .subtitle {
    position: absolute;
    left: 40px;
    right: 40px;
    top: 868px;
    margin: 0;
    text-align: center;
    font-family: "Roboto", sans-serif;
    font-weight: 300;
    font-size: 24px;
    line-height: 1.2;
    color: var(--subtitle);
  }
  .author {
    position: absolute;
    left: 0;
    right: 0;
    top: 930px;
    margin: 0;
    text-align: center;
    font-family: "Roboto Condensed", sans-serif;
    font-weight: 700;
    font-size: 52px;
    letter-spacing: 1px;
    text-transform: uppercase;
    color: var(--title-white);
  }
</style>
</head>
<body>
  <main class="canvas">
    <section class="cover">
      <div class="cover-art" role="img" aria-label="Smoky dark scene with a glowing cross in beams of light above a kneeling figure in silhouette"></div>
      <h1 class="title-block">
        <span class="title-line-1">Hollow</span>
        <span class="title-line-2">Altars</span>
      </h1>
      <p class="subtitle">Leaving Cold Pews Behind and Mending a<br>Wounded Heart Along the Road</p>
      <p class="author">Delia R. Marwick</p>
    </section>
  </main>
</body>
</html>
```